PROPERTY BROCHURE

Need an attractive layout and design for this multi-page brochure

Industry/Entity Type

Real Estate Development

Colors

Designer to choose colors to be used in the design.

```html
<!DOCTYPE html>
<html lang="en">
<head>
<meta charset="utf-8">
<title>Ridgeline Estates – Property Brochure Pages</title>
<link rel="stylesheet" href="https://fonts.googleapis.com/css2?family=Montserrat:wght@700&family=Roboto+Condensed:wght@700&family=Lato:ital,wght@0,400;0,700;1,400&family=PT+Sans:ital@1&display=swap">
<style>
  :root{
    --gold-dark:#a9843f;
    --gold:#c9a765;
    --gold-light:#ecdcb4;
    --ink:#141414;
    --grey:#d9d9d9;
    --grey-light:#f1f1f1;
    --table-head:#8b6a34;
    --chart-red:#c4161c;
    --paper:#ffffff;
  }
  *{margin:0;padding:0;box-sizing:border-box}
  html,body{width:900px;height:1200px;overflow:hidden;background:var(--paper)}
  .sheet{position:relative;width:900px;height:1200px;background:var(--paper)}
  .page{position:absolute;width:335px;height:475px;background:var(--paper);overflow:hidden;
        box-shadow:0 0 6px rgba(0,0,0,.25)}
  .page--front{left:87px;top:78px}
  .page--about{left:497px;top:78px}
  .page--city{left:87px;top:628px}
  .page--back{left:497px;top:628px}
  .page__art{position:absolute;left:0;top:0;width:335px;height:475px}
  .caption{position:absolute;width:335px;text-align:center;font-family:"PT Sans",sans-serif;
           font-style:italic;font-size:25px;color:var(--ink)}
  .caption--front{left:67px;top:574px}
  .caption--about{left:505px;top:574px}
  .caption--city{left:67px;top:1124px}
  .caption--back{left:505px;top:1124px}
  .brand{position:absolute;font-family:"Montserrat",sans-serif;font-weight:700;color:var(--ink);
         letter-spacing:-.3px;white-space:nowrap}
  .heading{position:absolute;font-family:"Roboto Condensed",sans-serif;font-weight:700;line-height:1}
  .body-copy{position:absolute;font-family:"Lato",sans-serif;font-style:italic;font-size:6.3px;
             line-height:1.35;color:#333;text-align:justify}
  .body-copy p+p{margin-top:5px}

  /* front */
  .front__brand{right:14px;top:96px;font-size:19px}
  .front__title{left:20px;top:176px;font-size:48px;color:var(--gold-dark);letter-spacing:1px}
  .front__subtitle{left:22px;top:219px;font-size:11.5px;color:var(--ink)}
  .facts{position:absolute;right:10px;top:413px;list-style:none;font-family:"Lato",sans-serif;
         font-weight:700;font-size:8.5px;color:var(--ink);text-align:right}
  .facts li{height:20px;display:flex;align-items:center;justify-content:flex-end;gap:6px}
  .facts li::after{content:"";width:10px;height:10px;border-radius:50%;background:var(--gold)}

  /* about */
  .about__title{left:30px;top:52px;font-size:19px;color:var(--ink)}
  .about__copy{left:30px;top:78px;width:275px}
  .about__brand{right:14px;top:441px;font-size:19px}

  /* city */
  .city__brand{left:15px;top:30px;font-size:15px}
  .city__name{left:15px;top:146px;color:var(--ink);font-family:"Montserrat",sans-serif;font-weight:700}
  .city__name span{display:block;line-height:1}
  .city__line1{font-size:24px}
  .city__line2{font-size:29px;color:var(--gold-dark)}
  .city__copy{left:15px;top:214px;width:172px}
  .stats{position:absolute;left:197px;top:61px;width:124px;border-collapse:collapse;
         font-family:"Lato",sans-serif;font-size:7px;text-align:center;color:var(--ink)}
  .stats th{background:var(--table-head);color:#fff;font-size:5.5px;font-weight:700;height:17px;
            border:1px solid #fff}
  .stats td{height:12.5px;border:1px solid #9b9b9b;background:#fff}
  .chart{position:absolute;left:197px;top:185px;width:124px;height:80px;border:1px solid #bdbdbd;background:#fff}
  .chart__title{position:absolute;top:4px;width:100%;text-align:center;font-family:"Lato",sans-serif;
                font-size:5px;color:#444}

  /* back */
  .back__brand{left:0;width:335px;text-align:center;top:84px;font-size:27px}
  .back__call{left:0;width:335px;text-align:center;top:432px;font-size:13px;color:var(--ink)}
  .back__web{position:absolute;left:0;width:335px;text-align:center;top:451px;
             font-family:"Lato",sans-serif;font-size:7.5px;letter-spacing:2px;color:var(--ink)}
</style>
</head>
<body>
<main class="sheet">

  <!-- Front cover -->
  <section class="page page--front" aria-label="Front cover">
    <svg class="page__art" viewBox="0 0 335 475" aria-hidden="false">
      <defs>
        <linearGradient id="goldA" x1="0" y1="0" x2="1" y2="0.4">
          <stop offset="0" stop-color="#b5914c"/><stop offset=".55" stop-color="#d8bd85"/><stop offset="1" stop-color="#efe2c0"/>
        </linearGradient>
        <linearGradient id="houseScene" x1="0" y1="0" x2="0" y2="1">
          <stop offset="0" stop-color="#f4f6f8"/><stop offset=".35" stop-color="#cfd9df"/>
          <stop offset=".7" stop-color="#a9503a"/><stop offset="1" stop-color="#4f7a36"/>
        </linearGradient>
        <linearGradient id="skyline" x1="0" y1="0" x2="0" y2="1">
          <stop offset="0" stop-color="#ffffff"/><stop offset="1" stop-color="#e6e6e6"/>
        </linearGradient>
      </defs>
      <polygon points="0,0 290,0 0,112" fill="url(#goldA)"/>
      <polygon points="0,112 290,0 335,0 335,12 0,124" fill="#fff"/>
      <polygon points="0,96 335,150 335,166 0,112" fill="#e4e4e4"/>
      <polygon points="0,124 335,170 335,177 0,131" fill="#151515"/>
      <rect x="0" y="232" width="335" height="190" fill="url(#houseScene)" role="img" aria-label="Photo of a two-storey brick family home with trees and lawn"/>
      <polygon points="0,400 335,365 335,475 0,475" fill="url(#skyline)"/>
      <polygon points="0,430 335,375 335,384 0,445" fill="#151515"/>
      <polygon points="0,445 335,384 335,392 0,452" fill="#fff"/>
    </svg>
    <div class="brand front__brand">ridgeline estates</div>
    <h1 class="heading front__title">PROPERTY</h1>
    <div class="heading front__subtitle">DEVELOPMENT INVESTMENTPROJECT SUMMARY</div>
    <ul class="facts">
      <li>Indicative Return: 43%</li>
      <li>Minimun Term: 12 months</li>
      <li>Minimun Investment: $250,000</li>
    </ul>
  </section>

  <!-- Inner page 1 -->
  <section class="page page--about" aria-label="Our business">
    <svg class="page__art" viewBox="0 0 335 475">
      <defs>
        <linearGradient id="goldB" x1="0" y1="0" x2="1" y2="1">
          <stop offset="0" stop-color="#b5914c"/><stop offset="1" stop-color="#ead9ad"/>
        </linearGradient>
        <linearGradient id="streetScene" x1="0" y1="0" x2="0" y2="1">
          <stop offset="0" stop-color="#dfe6ee"/><stop offset=".45" stop-color="#8e9aa6"/>
          <stop offset=".75" stop-color="#6b5d52"/><stop offset="1" stop-color="#9aa0a3"/>
        </linearGradient>
      </defs>
      <polygon points="200,0 335,0 335,150" fill="#e6e6e6"/>
      <polygon points="215,0 335,0 335,132" fill="url(#goldB)"/>
      <rect x="0" y="158" width="335" height="225" fill="url(#streetScene)" role="img" aria-label="Photo of modern townhouses along a residential street under a cloudy sky"/>
      <polygon points="0,400 335,360 335,475 0,475" fill="#f3f3f3"/>
      <polygon points="0,383 335,345 335,362 0,405" fill="#f3dede"/>
      <polygon points="0,420 335,368 335,378 0,438" fill="#151515"/>
      <polygon points="0,438 335,378 335,384 0,444" fill="#fff"/>
    </svg>
    <h2 class="heading about__title">OUR BUSINESS/WHAT WE DO</h2>
    <div class="body-copy about__copy">
      <p>Ridgeline Estates is a real estate development organisation that identifies and executes projects in metropolitan area of Melbourne. This projects offer investors the opportunity to obtain significant returns on investment above bank interest rates.</p>
      <p>Ridgeline Estates is committed to providing quality medium density accommodation solutions to address the housing shortage currently experienced by the Australian and New Zealand market.</p>
      <p>Our projects represent a seamless balance between the financial requirements of our investors and the housing needs of those living in the communities we touch.</p>
    </div>
    <div class="brand about__brand">ridgeline estates</div>
  </section>

  <!-- Inner page 2 -->
  <section class="page page--city" aria-label="Melbourne Victoria">
    <svg class="page__art" viewBox="0 0 335 475">
      <defs>
        <linearGradient id="goldC" x1="0" y1="1" x2="1" y2="0">
          <stop offset="0" stop-color="#a9843f"/><stop offset="1" stop-color="#e3cf9f"/>
        </linearGradient>
        <linearGradient id="suburbScene" x1="0" y1="0" x2="0" y2="1">
          <stop offset="0" stop-color="#ffffff"/><stop offset=".25" stop-color="#dfe5e8"/>
          <stop offset=".55" stop-color="#6f8a55"/><stop offset="1" stop-color="#9c9a92"/>
        </linearGradient>
      </defs>
      <rect x="0" y="0" width="335" height="270" fill="#f7f7f7"/>
      <polygon points="0,96 250,0 335,0 0,112" fill="url(#goldC)"/>
      <polygon points="0,112 335,0 335,270 0,270" fill="#fbfbfb"/>
      <rect x="0" y="272" width="335" height="203" fill="url(#suburbScene)" role="img" aria-label="Photo of a quiet suburban street with footpath, trees and fences"/>
    </svg>
    <div class="brand city__brand">ridgeline estates</div>
    <table class="stats">
      <tr><th>YEAR</th><th>POPULATION</th><th>GROWTH RATE</th></tr>
      <tr><td>2011</td><td>3850000</td><td>N/A</td></tr>
      <tr><td>2012</td><td>4090000</td><td>5.87%</td></tr>
      <tr><td>2013</td><td>4180000</td><td>2.20%</td></tr>
      <tr><td>2014</td><td>4250000</td><td>1.67%</td></tr>
      <tr><td>2015</td><td>4530000</td><td>6.60%</td></tr>
      <tr><td>2016</td><td>4670000</td><td>2.98%</td></tr>
      <tr><td>2017</td><td>4820000</td><td>3.21%</td></tr>
    </table>
    <div class="chart">
      <div class="chart__title">Victoria Population Growth</div>
      <svg width="124" height="80" viewBox="0 0 124 80">
        <g stroke="#e3e3e3" stroke-width=".5">
          <line x1="20" y1="18" x2="118" y2="18"/><line x1="20" y1="30" x2="118" y2="30"/>
          <line x1="20" y1="42" x2="118" y2="42"/><line x1="20" y1="54" x2="118" y2="54"/>
          <line x1="20" y1="66" x2="118" y2="66"/>
        </g>
        <polygon points="20,66 20,60 40,57 60,54 80,50 95,46 108,38 118,28 118,66" fill="var(--chart-red)"/>
      </svg>
    </div>
    <div class="city__name"><span class="city__line1">MELBOURNE</span><span class="city__line2">VICTORIA</span></div>
    <div class="body-copy city__copy">
      <p>Population growth in Melbourne is the strongest in the country at 3.2% over the year to June 2016 and is being driven by both strong overseas and interstate migration. Interstate migration increased 64% year-on-year (yr) to June 2016 according to the National Statistics Office. By the middle of this century it will overtake Sydney to be Australia's largest city.</p>
    </div>
  </section>

  <!-- Back cover -->
  <section class="page page--back" aria-label="Back cover">
    <svg class="page__art" viewBox="0 0 335 475">
      <defs>
        <linearGradient id="goldD" x1="0" y1="0" x2="1" y2="0">
          <stop offset="0" stop-color="#c7a35d"/><stop offset=".5" stop-color="#e8d5a6"/><stop offset="1" stop-color="#b89450"/>
        </linearGradient>
        <linearGradient id="stationScene" x1="0" y1="0" x2="0" y2="1">
          <stop offset="0" stop-color="#ffffff"/><stop offset=".3" stop-color="#e2e2e2"/><stop offset="1" stop-color="#cfcfcf"/>
        </linearGradient>
      </defs>
      <rect x="0" y="120" width="335" height="250" fill="url(#stationScene)" role="img" aria-label="Faded black and white photo of a historic domed railway station"/>
      <polygon points="0,378 335,318 335,475 0,475" fill="#e0e0e0"/>
      <polygon points="0,394 335,328 335,344 0,410" fill="#151515"/>
      <polygon points="0,410 335,344 335,475 0,475" fill="url(#goldD)"/>
    </svg>
    <div class="brand back__brand">ridgeline estates</div>
    <div class="heading back__call">CALL US TODAY-123 1234 123</div>
    <div class="back__web">visit us-www.ridgelineestates.com</div>
  </section>

  <p class="caption caption--front">front page</p>
  <p class="caption caption--about">inner page1</p>
  <p class="caption caption--city">inner page2</p>
  <p class="caption caption--back">back page</p>
</main>
</body>
</html>
```